Postcard Design

Bluestone Haven Group Company Inc, is a air duct cleaning, dryer vent cleaning & pressure washing company, we would like this postcard to focus fully on our pressure washing specials for the season.

```html
<!DOCTYPE html>
<html lang="en">
<head>
<meta charset="utf-8">
<title>Bluestone Haven Group – Power Washing Postcard</title>
<link rel="stylesheet" href="https://fonts.googleapis.com/css2?family=Lato:ital,wght@0,400;0,700;1,700&display=swap">
<style>
  :root {
    --page-bg: #ecebe8;
    --charcoal: #3b3b3c;
    --teal: #3bb6c0;
    --teal-soft: #6fcbd1;
    --ink: #333333;
    --white: #ffffff;
    --card-light: #fbfbfb;
    --card-shade: #dcdcdc;
  }
  * { box-sizing: border-box; margin: 0; padding: 0; }
  html, body {
    width: 1200px; height: 825px; overflow: hidden;
    background: var(--page-bg);
    font-family: "Lato", Arial, sans-serif;
  }
  .postcard {
    position: absolute; left: 98px; top: 138px;
    width: 1005px; height: 552px; overflow: hidden;
    background: linear-gradient(180deg, var(--card-light) 0%, #f1f1f1 60%, var(--card-shade) 100%);
    box-shadow: 0 4px 14px rgba(0,0,0,.18);
  }
  .backdrop { position: absolute; inset: 0; width: 1005px; height: 552px; }
  .brand-name {
    position: absolute; left: 52px; top: 58px; width: 340px;
    color: var(--white); font-weight: 700; font-size: 38px; line-height: 1.1;
  }
  .photo {
    position: absolute; border-radius: 50%;
    border: 9px solid #ececec;
    box-shadow: 0 3px 10px rgba(0,0,0,.25);
  }
  .photo--driveway {
    left: 45px; top: 190px; width: 258px; height: 268px;
    background: linear-gradient(160deg, #4f6b45 0%, #7d8a7a 35%, #a9aeae 65%, #8f9595 100%);
  }
  .photo--pavers {
    left: 304px; top: 188px; width: 178px; height: 178px;
    background: linear-gradient(135deg, #b8a27c 0%, #cdbd9c 50%, #e6e0d4 100%);
  }
  .headline {
    position: absolute; right: 52px; top: 24px;
    color: var(--white); font-weight: 700; font-size: 58px; letter-spacing: .3px;
  }
  .intro {
    position: absolute; right: 58px; top: 98px; width: 480px;
    text-align: right; color: var(--ink); font-size: 16.5px; line-height: 1.3;
  }
  .phone {
    position: absolute; right: 55px; top: 258px;
    color: var(--ink); font-weight: 700; font-size: 33px;
  }
  .estimate-pill {
    position: absolute; left: 517px; top: 314px; width: 488px; height: 53px;
    background: var(--teal-soft); border-radius: 27px 0 0 27px;
    display: flex; align-items: center; justify-content: flex-end; padding-right: 52px;
    color: var(--ink); font-style: italic; font-weight: 700; font-size: 21px;
  }
  .services {
    position: absolute; top: 393px; list-style: none;
    color: var(--ink); font-size: 21px; line-height: 26.5px; text-align: right;
  }
  .services--left { right: 316px; }
  .services--right { right: 60px; }
  .services li::after {
    content: ""; display: inline-block; width: 11px; height: 11px; margin-left: 11px;
    border-radius: 50%; background: #a9e0e5; vertical-align: 2px;
  }
  .footer-rule { position: absolute; left: 0; top: 509px; width: 100%; height: 8px; background: var(--charcoal); }
  .footer-band { position: absolute; left: 0; top: 517px; width: 100%; height: 35px; background: var(--teal-soft); }
</style>
</head>
<body>
  <main class="postcard">
    <svg class="backdrop" viewBox="0 0 1005 552" aria-hidden="true">
      <defs>
        <linearGradient id="tealFade" x1="0" y1="0" x2="0" y2="1">
          <stop offset="0" stop-color="#2fb0bb"/>
          <stop offset="1" stop-color="#7fd0d6"/>
        </linearGradient>
      </defs>
      <path class="panel-dark" d="M0 0 H428 C398 90 382 170 410 255 C300 245 150 240 0 240 Z" fill="#3b3b3c"/>
      <path class="panel-teal" d="M455 0 H1005 V172 C850 150 660 190 490 262 C425 195 418 85 455 0 Z" fill="url(#tealFade)"/>
      <path class="swoosh" d="M470 270 C640 208 850 200 1005 212 V232 C850 222 660 232 470 270 Z" fill="#3b3b3c"/>
    </svg>

    <div class="brand-name">Bluestone Haven Group</div>

    <div class="photo photo--driveway" role="img" aria-label="Worker in rubber boots pressure washing a stone driveway"></div>
    <div class="photo photo--pavers" role="img" aria-label="Pressure washer wand cleaning brick pavers"></div>

    <h1 class="headline">Power Washing</h1>
    <p class="intro">With a 4500 PSI heated truck-mounted pressure washer, we can make any project look brand new.</p>

    <p class="phone">Phone: (555) 482-0193</p>
    <div class="estimate-pill">Call us for a free estimate on your project!</div>

    <ul class="services services--left">
      <li>Fleet Washes</li>
      <li>Whole Homes</li>
      <li>Apartments &amp; Drive Thrus</li>
    </ul>
    <ul class="services services--right">
      <li>Sidewalks</li>
      <li>Much More!</li>
      <li>Commercial Building</li>
    </ul>

    <div class="footer-rule"></div>
    <div class="footer-band"></div>
  </main>
</body>
</html>
```